Software allocation system needs a business card design

We need a business card designed for our software platform - www.rostellio.com.au

At the moment the logo and website is all black and white, we are happy for suggestions on implementing some colour throughout either the logo or business card.

Industry/Entity Type

Software

Font styles to use
Sans Serif

Colors

Designer to choose colors to be used in the design.

```html
<!DOCTYPE html>
<html lang="en">
<head>
<meta charset="utf-8">
<title>Rostellio Business Card</title>
<link rel="stylesheet" href="https://fonts.googleapis.com/css2?family=Open+Sans:wght@400;600&display=swap">
<style>
  :root {
    --page-bg: #e8e5e1;
    --card-white: #ffffff;
    --frame-dark: #2b2b2b;
    --tab-grey: #7a7a7a;
    --tab-edge: #f2f2f2;
    --ink: #1e1e1e;
    --ink-soft: #333333;
  }
  * { box-sizing: border-box; margin: 0; padding: 0; }
  html, body {
    width: 1200px;
    height: 939px;
    overflow: hidden;
    background: var(--page-bg);
    font-family: "Open Sans", Arial, sans-serif;
  }
  .business-card {
    position: absolute;
    left: 100px;
    top: 184px;
    width: 1000px;
    height: 571px;
    background: var(--card-white);
    box-shadow: 0 18px 40px rgba(0,0,0,0.18);
    overflow: hidden;
  }
  .card-frame { position: absolute; inset: 0; }
  .holder-name {
    position: absolute;
    left: 62px;
    top: 58px;
    font-size: 44px;
    font-weight: 400;
    color: var(--ink);
    letter-spacing: 0.5px;
    line-height: 1;
  }
  .holder-role {
    position: absolute;
    left: 64px;
    top: 116px;
    font-size: 17px;
    color: var(--ink-soft);
  }
  .contact-list {
    position: absolute;
    left: 60px;
    top: 200px;
    list-style: none;
  }
  .contact-item {
    display: flex;
    align-items: center;
    gap: 16px;
    margin-bottom: 30px;
  }
  .contact-icon { width: 26px; height: 26px; flex: none; fill: var(--ink); }
  .contact-lines {
    font-size: 19px;
    line-height: 1.3;
    color: var(--ink);
  }
  .brand-name {
    position: absolute;
    left: 470px;
    top: 226px;
    display: flex;
    align-items: center;
    gap: 18px;
    font-size: 64px;
    font-weight: 400;
    letter-spacing: 6px;
    color: var(--ink);
    line-height: 1;
  }
  .brand-dot {
    width: 22px;
    height: 22px;
    border-radius: 50%;
    background: var(--ink);
  }
</style>
</head>
<body>
  <article class="business-card">
    <svg class="card-frame" viewBox="0 0 1000 571" width="1000" height="571" aria-hidden="true">
      <!-- frame bands -->
      <rect x="0" y="0" width="1000" height="26" fill="var(--frame-dark)"/>
      <rect x="0" y="545" width="1000" height="26" fill="var(--frame-dark)"/>
      <rect x="0" y="0" width="14" height="571" fill="var(--frame-dark)"/>
      <rect x="986" y="0" width="14" height="571" fill="var(--frame-dark)"/>
      <!-- top tab -->
      <path d="M36 0 H310 V34 Q310 48 296 48 H50 Q36 48 36 34 Z" fill="var(--tab-grey)" stroke="var(--tab-edge)" stroke-width="3"/>
      <!-- bottom tab -->
      <path d="M170 571 V532 Q170 518 184 518 H440 Q454 518 454 532 V571 Z" fill="var(--tab-grey)" stroke="var(--tab-edge)" stroke-width="3"/>
      <!-- name pointer -->
      <path d="M0 92 H34 L50 114 L34 136 H0 Z" fill="var(--frame-dark)"/>
    </svg>

    <h1 class="holder-name">JOHN DOE</h1>
    <p class="holder-role">Managing Director</p>

    <ul class="contact-list">
      <li class="contact-item">
        <svg class="contact-icon" viewBox="0 0 24 24" aria-hidden="true"><path d="M12 3 L2 12 H5 V21 H10 V15 H14 V21 H19 V12 H22 Z"/></svg>
        <span class="contact-lines">48 Harbour Lane, Sydney<br>2000 Australia</span>
      </li>
      <li class="contact-item">
        <svg class="contact-icon" viewBox="0 0 24 24" aria-hidden="true"><circle cx="12" cy="12" r="9.5" fill="none" stroke="currentColor" stroke-width="2"/><ellipse cx="12" cy="12" rx="4" ry="9.5" fill="none" stroke="currentColor" stroke-width="1.6"/><path d="M3 9 H21 M3 15 H21" stroke="currentColor" stroke-width="1.6"/></svg>
        <span class="contact-lines">johndoe@rostellio.com.au<br>www.rostellio.com.au</span>
      </li>
      <li class="contact-item">
        <svg class="contact-icon" viewBox="0 0 24 24" aria-hidden="true"><path d="M6.6 10.8 C8 13.6 10.4 16 13.2 17.4 L15.4 15.2 C15.7 14.9 16.1 14.8 16.4 14.9 C17.5 15.3 18.7 15.5 20 15.5 C20.6 15.5 21 15.9 21 16.5 V20 C21 20.6 20.6 21 20 21 C10.6 21 3 13.4 3 4 C3 3.4 3.4 3 4 3 H7.5 C8.1 3 8.5 3.4 8.5 4 C8.5 5.3 8.7 6.5 9.1 7.6 C9.2 7.9 9.1 8.3 8.8 8.6 Z"/></svg>
        <span class="contact-lines">888-020-440-176-09<br>888-020-440-176-09</span>
      </li>
    </ul>

    <div class="brand-name"><span class="brand-dot"></span>ROSTELLIO</div>
  </article>
</body>
</html>
```